Mobile and Web design for Remote Skin Condition Service

A new web service that allows patients to upload photos for doctors to review. I need the designs for both mobile (NOT native app) and desktop versions. Key pages are provided in the mockups, and all major form elements are required.
Overall branding and design needed.

We are building an online system that allows patients to connect with a skin doctors.

Users will access the website (typically, but not exclusively via a mobile phone), register, upload photos, answer a few questions and pay to submit their details to a doctor.

The doctor will access the website via a desktop browser and review the case.

The patient’s user flow should be optimised for mobile. It should be usable on desktop too.

The doctor’s user flow should be optimised for desktop. It should be usable on mobile too.

Currently there are no branding restrictions, and no logo, so please be creative.

The site has to look professional, clean and easy to use.
There will be limited text on the pages.
Buttons should be prominent - but they should also obviously be buttons.

Attached are a selection of screens showing most of the functionality of the process - it is not all of the screens of the process but should give the developers enough range and examples.

Target Market(s)

Any user with a skin condition

Industry/Entity Type

Healthcare

Number of Pages Required

5+ page

Colors

Designer to choose colors to be used in the design.

Requirements
Must have
• Mobile and desktop versions of the key pages as per the brief.
• Should be obvious to use - eg the photo upload and camera functions should be standard

```html
<!DOCTYPE html>
<html lang="en">
<head>
<meta charset="utf-8">
<title>DermaLink – Web and Mobile Screens</title>
<link href="https://fonts.googleapis.com/css2?family=Poppins:wght@400;500&display=swap" rel="stylesheet">
<style>
:root{
  --blue:#3a97dc;
  --blue-dark:#2a80c4;
  --band:#eaf4fb;
  --green:#8cb833;
  --ink:#2b2b2b;
  --muted:#555;
  --white:#fff;
  --rule:#d0d0d0;
}
*{box-sizing:border-box;margin:0;padding:0}
html,body{width:1200px;height:971px;overflow:hidden;background:var(--white);font-family:'Poppins',sans-serif;color:var(--ink)}
.canvas{position:relative;width:1200px;height:971px}

.page{position:absolute;background:var(--white);box-shadow:0 1px 6px rgba(0,0,0,.18)}
.page-header{position:absolute;left:0;top:0;width:100%;height:42px;background:var(--band);border-bottom:2px solid var(--green)}
.brand{position:absolute;display:flex;align-items:center;gap:5px;color:var(--blue);font-weight:400;font-size:12.5px;white-space:nowrap}
.brand-dot{width:14px;height:14px;border-radius:50%;background:var(--blue)}
.welcome{position:absolute;color:var(--blue);font-weight:500;font-size:11.5px;white-space:nowrap}
.footer-rule{position:absolute;height:1px;background:var(--rule)}
.footer-text{position:absolute;font-size:6.6px;color:var(--ink);text-align:center}

.photo{position:absolute;box-shadow:0 1px 4px rgba(0,0,0,.25)}
.photo-consult{background:linear-gradient(135deg,#c9b7a8 0%,#e3cfc1 40%,#8aa6c4 75%,#d8dfe6 100%)}
.photo-elbow{background:linear-gradient(135deg,#d8d4d0 0%,#8fb2ad 45%,#6d5a52 75%,#cfd3d6 100%)}
.copy{position:absolute;font-size:5.6px;line-height:10.5px;color:var(--muted);text-align:justify}
.copy p+p{margin-top:6px}

.btn{position:absolute;background:var(--blue);color:var(--white);border:1px solid var(--white);box-shadow:0 0 0 1px var(--blue),0 2px 3px rgba(0,0,0,.25);display:flex;align-items:center;justify-content:center;font-weight:500;border-radius:2px;white-space:nowrap}

.dark-box{position:absolute;background:linear-gradient(120deg,#272321 0%,#3c3431 45%,#5a4a44 70%,#2c2826 100%);box-shadow:0 2px 6px rgba(0,0,0,.35)}
.dark-box .texture{position:absolute;inset:0;background:radial-gradient(ellipse at 65% 55%,rgba(150,120,105,.35),transparent 60%)}
.bar{position:absolute;background:var(--blue);color:var(--white);border:1px solid var(--white);display:flex;align-items:center;justify-content:center;font-weight:500;font-size:12.5px}
.field{position:absolute;background:var(--white);border:1px solid #cfcfcf;border-radius:2px}
.label{position:absolute;color:var(--white);font-size:8px;line-height:10px;text-align:right}
.link{position:absolute;color:var(--blue);font-size:6.6px;text-decoration:underline}

.screen{position:absolute;background:var(--white);box-shadow:0 1px 6px rgba(0,0,0,.2);overflow:hidden}
.screen-header{position:absolute;left:0;top:0;width:100%;height:63px;background:var(--band)}
.screen .brand{font-size:14px;left:0;width:100%;justify-content:center;top:27px}
.screen-welcome{position:absolute;left:0;width:100%;text-align:center;color:var(--blue);font-weight:500;font-size:11px;top:77px;white-space:nowrap}
.screen-sub{position:absolute;left:0;width:100%;text-align:center;font-size:8px;top:99px}
.card{position:absolute;border:1px solid var(--blue);border-radius:2px}
.steps{position:absolute;list-style:none}
.step{display:flex;align-items:flex-start;gap:4px;font-size:6.4px;line-height:9px;height:21px}
.step-num{flex:none;width:13px;height:13px;border-radius:50%;color:var(--white);font-size:6px;display:flex;align-items:center;justify-content:center;margin-top:-2px}
.step-num.blue{background:var(--blue)}
.step-num.grey{background:#555}
.play{position:absolute}
.screen-foot{position:absolute;left:0;width:100%;text-align:center;font-size:5.6px;font-family:Georgia,serif}
.centered{position:absolute;left:0;width:100%;text-align:center}
.checkbox{position:absolute;width:7px;height:7px;border:1px solid #777;background:var(--white)}
</style>
</head>
<body>
<div class="canvas">

  <section class="page" style="left:43px;top:38px;width:491px;height:359px">
    <header class="page-header">
      <div class="brand" style="left:46px;top:14px"><span class="brand-dot"></span>DermaLink</div>
      <div class="welcome" style="left:186px;top:13px">Welcome To DermaLink!</div>
    </header>
    <div class="photo photo-consult" style="left:46px;top:67px;width:210px;height:152px" role="img" aria-label="Photo of a doctor examining a smiling girl's cheek while her mother watches"></div>
    <div class="copy" style="left:270px;top:74px;width:173px">
      <p>Nemo enim ipsam voluptatem quia voluptas sit aspernatur aut odit aut fugit, sed quia consequuntur magni dolores eos qui ratione voluptatem sequi nesciunt. Neque porro quisquam est, qui dolorem ipsum quia dolor sit amet, consectetur, adipisci velit, sed quia non numquam eius modi tempora incidunt ut labore et dolore magnam aliquam quaerat voluptatem.</p>
      <p>Ut enim ad minima veniam, quis nostrum exercitationem ullam corporis suscipit laboriosam, nisi ut aliquid ex ea commodi consequatur. Quis autem vel eum iure reprehenderit qui in ea voluptate velit esse quam nihil molestiae consequatur, vel illum qui dolorem eum fugiat quo voluptas. Sed ut perspiciatis unde omnis iste natus error sit voluptatem.</p>
    </div>
    <div class="btn" style="left:197px;top:239px;width:97px;height:25px;font-size:9.5px">Free Consultation</div>
    <p class="copy" style="left:46px;top:280px;width:400px;text-align:center">Nam libero tempore, cum soluta nobis est eligendi optio cumque nihil impedit quo minus id quod maxime placeat facere possimus, omnis voluptas assumenda est, omnis dolor repellendus. Temporibus autem quibusdam et aut officiis debitis aut rerum necessitatibus saepe eveniet ut et voluptates repudiandae sint et molestiae non recusandae. Itaque earum rerum hic tenetur a sapiente delectus, ut aut reiciendis</p>
    <div class="footer-rule" style="left:46px;top:328px;width:400px"></div>
    <p class="footer-text" style="left:46px;top:339px;width:400px">Copyrights @ 2020 DermaLink. All Rights Reserved.</p>
  </section>

  <section class="page" style="left:554px;top:38px;width:491px;height:426px">
    <header class="page-header">
      <div class="brand" style="left:46px;top:14px"><span class="brand-dot"></span>DermaLink</div>
      <div class="welcome" style="left:186px;top:13px">Welcome To DermaLink!</div>
    </header>
    <div class="dark-box" style="left:97px;top:65px;width:296px;height:305px">
      <div class="texture" role="img" aria-label="Darkened close-up photo of a doctor's hands examining skin"></div>
      <div class="bar" style="left:13px;top:13px;width:269px;height:28px">My Account</div>
      <div class="label" style="left:0;top:64px;width:43px">Name</div>
      <div class="field" style="left:50px;top:58px;width:90px;height:21px"></div>
      <div class="label" style="left:140px;top:64px;width:43px">Email</div>
      <div class="field" style="left:190px;top:58px;width:90px;height:21px"></div>
      <div class="label" style="left:0;top:90px;width:43px">GMC Number</div>
      <div class="field" style="left:50px;top:89px;width:90px;height:21px"></div>
      <div class="label" style="left:130px;top:90px;width:53px">Mobile Ph Number</div>
      <div class="field" style="left:190px;top:89px;width:90px;height:21px"></div>
      <div class="btn" style="left:50px;top:121px;width:57px;height:19px;font-size:7px">Update Details</div>
      <div class="bar" style="left:13px;top:160px;width:269px;height:28px">Change Password</div>
      <div class="label" style="left:0;top:206px;width:43px">Old Password</div>
      <div class="field" style="left:50px;top:205px;width:90px;height:21px"></div>
      <div class="label" style="left:130px;top:206px;width:53px">New Password</div>
      <div class="field" style="left:190px;top:205px;width:90px;height:21px"></div>
      <div class="label" style="left:0;top:237px;width:43px">Confirm Password</div>
      <div class="field" style="left:50px;top:236px;width:90px;height:21px"></div>
      <div class="btn" style="left:50px;top:268px;width:66px;height:19px;font-size:7px">Update Password</div>
    </div>
    <div class="footer-rule" style="left:46px;top:395px;width:400px"></div>
    <p class="footer-text" style="left:46px;top:406px;width:400px">Copyrights @ 2020 DermaLink. All Rights Reserved.</p>
  </section>

  <section class="page" style="left:43px;top:422px;width:491px;height:339px">
    <header class="page-header">
      <div class="brand" style="left:46px;top:14px"><span class="brand-dot"></span>DermaLink</div>
      <div class="welcome" style="left:186px;top:13px">Welcome To DermaLink!</div>
    </header>
    <div class="dark-box" style="left:97px;top:76px;width:296px;height:200px">
      <div class="texture" role="img" aria-label="Darkened close-up photo of a doctor's hands examining skin"></div>
      <div class="bar" style="left:3px;top:3px;width:290px;height:26px">Doctor Login</div>
      <div class="label" style="left:25px;top:46px;text-align:left">Email</div>
      <div class="field" style="left:25px;top:61px;width:245px;height:21px"></div>
      <div class="label" style="left:25px;top:92px;text-align:left">Password</div>
      <div class="field" style="left:25px;top:107px;width:245px;height:21px"></div>
      <div class="btn" style="left:25px;top:140px;width:46px;height:22px;font-size:8.5px">Login</div>
      <div class="link" style="left:25px;top:172px">Forgot Password?</div>
    </div>
    <div class="footer-rule" style="left:46px;top:307px;width:400px"></div>
    <p class="footer-text" style="left:46px;top:318px;width:400px">Copyrights @ 2020 DermaLink. All Rights Reserved.</p>
  </section>

  <section class="screen" style="left:578px;top:513px;width:144px;height:409px">
    <header class="screen-header"><div class="brand"><span class="brand-dot"></span>DermaLink</div></header>
    <h1 class="screen-welcome">Welcome To DermaLink!</h1>
    <p class="screen-sub">The Next Steps</p>
    <div class="card" style="left:6px;top:119px;width:134px;height:261px">
      <ol class="steps" style="left:4px;top:14px;width:128px">
        <li class="step"><span class="step-num blue">01</span>Take or upload 3 photos</li>
        <li class="step"><span class="step-num grey">02</span>Tell us a little about yourself</li>
        <li class="step"><span class="step-num blue">03</span><span style="white-space:nowrap">Answer a few medical questions</span></li>
        <li class="step"><span class="step-num grey">04</span>Make a secure online payment</li>
        <li class="step"><span class="step-num blue">05</span>Wait just 24 hours for your diagnosis</li>
      </ol>
      <div class="photo photo-elbow" style="left:6px;top:127px;width:121px;height:95px;box-shadow:none" role="img" aria-label="Video still of a doctor checking an older woman's elbow"></div>
      <svg class="play" style="left:53px;top:161px" width="27" height="27" viewBox="0 0 27 27" aria-hidden="true">
        <circle cx="13.5" cy="13.5" r="12" fill="rgba(0,0,0,.25)" stroke="#fff" stroke-width="1.6"/>
        <path d="M10.5 8.5 L18.5 13.5 L10.5 18.5 Z" fill="#fff"/>
      </svg>
      <div class="btn" style="left:30px;top:233px;width:72px;height:17px;font-size:7px">Ready To Start?</div>
    </div>
    <p class="screen-foot" style="top:393px">Copyrights @ 2020 DermaLink. All Rights Reserved.</p>
  </section>

  <section class="screen" style="left:786px;top:513px;width:144px;height:373px">
    <header class="screen-header"><div class="brand"><span class="brand-dot"></span>DermaLink</div></header>
    <h1 class="screen-welcome">Welcome To DermaLink!</h1>
    <p class="screen-sub" style="font-size:7px">Already Registered? Login Here!</p>
    <div class="card" style="left:5px;top:119px;width:134px;height:227px">
      <p class="centered" style="top:9px;font-size:7.5px;font-weight:500">Nam Libero Tempore</p>
      <p class="centered" style="top:25px;padding:0 7px;font-size:5.3px;line-height:9.8px;color:var(--muted)">At vero eos et accusamus et iusto odio dignissimos ducimus qui blanditiis praesentium voluptatum deleniti atque corrupti quos dolores et quas molestias excepturi sint occaecati cupiditate.</p>
      <p class="centered" style="top:82px;padding:0 14px;font-size:6px;line-height:9.6px;color:var(--blue)">This service works best from a smart phone</p>
      <p class="centered" style="top:106px;padding:0 10px;font-size:5.3px;line-height:9.8px">These are our Terms and Conditions and Privacy Policy</p>
      <p class="centered" style="top:131px;font-size:6px;color:var(--blue);text-decoration:underline">Terms and Conditions</p>
      <p class="centered" style="top:141px;font-size:6px;color:var(--blue);text-decoration:underline">Privacy Policy</p>
      <span class="checkbox" style="left:6px;top:158px"></span>
      <p style="position:absolute;left:17px;top:154px;width:112px;font-size:4.4px;line-height:8.4px;color:var(--muted)">I understand by continuing, I am agreeing to the Terms and Conditions of Service and that my case will be passed to doctors in order to diagnose my condition.</p>
      <div class="btn" style="left:30px;top:197px;width:72px;height:17px;font-size:7px">Get Diagnosed</div>
    </div>
    <p class="screen-foot" style="top:357px">Copyrights @ 2020 DermaLink. All Rights Reserved.</p>
  </section>

  <section class="screen" style="left:996px;top:513px;width:144px;height:318px">
    <header class="screen-header"><div class="brand"><span class="brand-dot"></span>DermaLink</div></header>
    <h1 class="screen-welcome">Welcome To DermaLink!</h1>
    <div class="photo photo-consult" style="left:7px;top:103px;width:68px;height:90px;box-shadow:none" role="img" aria-label="Photo of a doctor examining a smiling girl's cheek"></div>
    <p class="copy" style="left:82px;top:102px;width:58px;text-align:left;font-size:5px;line-height:10.2px">Nam libero tempore, cum soluta nobis est eligendi optio cumque nihil impedit quo minus id quod maxime placeat facere possimus, omnis voluptas assumenda est.</p>
    <p class="copy" style="left:7px;top:206px;width:130px;font-size:5.3px;line-height:9.2px">At vero eos et accusamus et iusto odio dignissimos ducimus qui blanditiis praesentium voluptatum deleniti atque corrupti quos dolores et quas molestias excepturi sint occaecati cupiditate non provident, similique.</p>
    <div class="btn" style="left:35px;top:264px;width:72px;height:17px;font-size:7px">Free Consultation</div>
    <p class="screen-foot" style="top:298px">Copyrights @ 2020 DermaLink. All Rights Reserved.</p>
  </section>

</div>
</body>
</html>
```